Wir suchen ein kreatives Einladungskarten-Design
Zielgruppe
Terminierung / Organisation für Steuerberater, Rechtsanwälte Wirtschaftsprüfer und Notare.
Aufgabenstellung
Nicht verspielt, ansprechend, jung, kreativ,
20 jähriges Firmenjubiläum am 30.11.2018 um 17:00 Uhr
Motto: Feuer (in dir muss brennen was du in anderen entzünden willst)
Dies sollte aber sehr elegant und nicht kitschig dargestellt werden.
Eventuell werden wir zur Einladung ein scharfes Gewürz beilegen
Save the date
And celebrate with us
20 Jahre MRW
Freitag, 30.11.18, 17:00 Uhr
Seien Sie dabei, wir freuen uns auf Sie!
Wir bitten um Rückmeldung bis spätestens 31.10.18
Kornstraße 27 84217 Cham

```html
<!DOCTYPE html>
<html lang="de">
<head>
<meta charset="utf-8">
<title>Einladung Firmenjubiläum</title>
<link href="https://fonts.googleapis.com/css2?family=Cinzel:wght@400;600;700&display=swap" rel="stylesheet">
<style>
  :root {
    --sheet-bg: #d1d1d0;
    --stone-dark: #232325;
    --stone-mid: #3a3a3d;
    --gold: #d9a94a;
    --gold-deep: #8a5c16;
    --ember: #ff8a1e;
    --ember-deep: #b8320a;
    --label-ink: #222;
    --photo-left: #5a4e4c;
    --photo-mid: #c7732a;
    --photo-right: #7a3a18;
  }
  * { box-sizing: border-box; margin: 0; padding: 0; }
  html, body { width: 720px; height: 1200px; overflow: hidden; }
  body {
    background: var(--sheet-bg);
    font-family: "Cinzel", "Times New Roman", serif;
    display: flex;
    flex-direction: column;
    justify-content: center;
    align-items: center;
  }
  .side-label {
    width: 680px;
    font-size: 9px;
    letter-spacing: 0.04em;
    color: var(--label-ink);
    margin: 0 0 4px;
  }
  .side-label + .card { margin-bottom: 14px; }
  .card {
    position: relative;
    width: 680px;
    height: 317px;
    overflow: hidden;
    background:
      radial-gradient(ellipse at 20% 30%, rgba(90,90,94,0.35), transparent 55%),
      radial-gradient(ellipse at 80% 70%, rgba(80,80,84,0.3), transparent 60%),
      linear-gradient(160deg, var(--stone-mid), var(--stone-dark));
  }
  .gold-text {
    color: var(--gold);
    text-shadow: 0 1px 0 var(--gold-deep), 0 2px 3px rgba(0,0,0,0.85);
  }
  /* Front */
  .motto {
    position: absolute;
    top: 8px;
    left: 0;
    right: 0;
    text-align: center;
    font-weight: 400;
    line-height: 1.1;
  }
  .motto-line { display: block; font-size: 23px; letter-spacing: 1.4px; }
  .motto-line--second { font-size: 24px; letter-spacing: 1.8px; }
  .motto-fire {
    font-size: 31px;
    font-weight: 700;
    letter-spacing: 2px;
    color: var(--ember);
    text-shadow: 0 0 4px var(--ember-deep), 0 0 10px rgba(255,90,0,0.6), 0 2px 2px #000;
  }
  .hero-visual {
    position: absolute;
    left: 0;
    top: 82px;
    width: 680px;
    height: 235px;
    background: linear-gradient(90deg, var(--photo-left), var(--photo-mid) 60%, var(--photo-right));
  }
  /* Back */
  .logo-slot {
    position: absolute;
    top: 0;
    left: 260px;
    width: 160px;
    height: 76px;
    background: #fff;
    box-shadow: 0 3px 6px rgba(0,0,0,0.5);
    display: flex;
    align-items: center;
    justify-content: center;
    font-size: 12px;
    color: #111;
  }
  .event-details {
    position: absolute;
    top: 110px;
    left: 0;
    right: 0;
    text-align: center;
  }
  .event-intro { display: block; font-size: 28px; line-height: 36px; }
  .event-title { display: block; font-size: 40px; line-height: 44px; }
  .event-date { display: block; font-size: 29px; line-height: 40px; }
</style>
</head>
<body>
  <p class="side-label">VORDERSEITE</p>
  <section class="card card--front">
    <h1 class="motto gold-text">
      <span class="motto-line">IN DIR MUSS <span class="motto-fire">BRENNEN</span>,</span>
      <span class="motto-line motto-line--second">WAS DU IN ANDEREN ENTZÜNDEN WILLST.</span>
    </h1>
    <div class="hero-visual" role="img" aria-label="Foto: Mann in Hemd und Krawatte, der einen großen Feuerstoß ausatmet"></div>
  </section>

  <p class="side-label">RÜCKSEITE</p>
  <section class="card card--back">
    <div class="logo-slot">LOGO</div>
    <div class="event-details gold-text">
      <span class="event-intro">WIR FEIERN</span>
      <span class="event-title">20-JÄHRIGES<br>FIRMENJUBILÄUM</span>
      <span class="event-date">30.11.2018 | 17:00 UHR</span>
    </div>
  </section>
</body>
</html>
```